Herbal tea shop web designing - Brewvine

We need a business-charity purpose online shop selling premium herbal teas with a tagline "Healthy with a heart" where all the raw materials are being purchased from Indonesian local farmers in order to give them sustainable employment. Every 20% from the total amount of the customer's purchase from our website always goes back to their communities to help build better sanitation, education or whatever they need. We need page to blog too and another page for customers to interact and share their thought. we expect an eye catching simple earthy (maybe a bit rustic) design with some brush lettering font in some parts. Thank you.

Target Market(s)

-Tea Lovers
-Anyone with body weight issues or any health issues in general

Industry/Entity Type

Home Health Care

Number of Pages Required

5+ page

Font styles to use
Other font styles liked:
• brush lettering font in some parts

Requirements
Must have
• - Brush lettering font
• -Simple, a bit rustic design with some nice watercolor touch
• -Blogging Page
• -catchy yet fancy and elegant E-commerce page
Nice to have
• Well, I will let the designers use their skills and imaginations to the fullest.

```html
<!DOCTYPE html>
<html lang="en">
<head>
<meta charset="utf-8">
<title>Herbal Teas — Healthy With a Heart</title>
<link href="https://fonts.googleapis.com/css2?family=Roboto:wght@300;400;500;700&family=Dancing+Script:wght@700&display=swap" rel="stylesheet">
<style>
:root{
  --green:#2dbe6c;
  --green-dark:#25a85e;
  --ink:#2b2b2b;
  --text:#555a5f;
  --muted:#8a8f94;
  --line:#ececec;
  --soft:#f6f8f7;
  --night:#26272b;
  --night-deep:#1f2024;
  --white:#ffffff;
}
*{box-sizing:border-box;margin:0;padding:0}
html,body{width:1200px;height:2341px;overflow:hidden}
body{font-family:"Roboto",Arial,sans-serif;color:var(--text);background:var(--white);position:relative}
.abs{position:absolute}
a{color:inherit;text-decoration:none}

/* top bar */
.topbar{left:0;top:0;width:1200px;height:39px;background:var(--green)}
.topbar .social{left:89px;top:7px;display:flex;gap:6px}
.topbar .social span{width:26px;height:26px;background:rgba(255,255,255,.18);display:block}
.topbar .account{right:89px;top:0;height:39px;display:flex;gap:34px;align-items:center;color:var(--white);font-size:12px}
.topbar .account span{display:flex;align-items:center;gap:7px}
.topbar .account i{width:10px;height:10px;background:var(--white);border-radius:2px;display:block}

/* header */
.header{left:0;top:39px;width:1200px;height:86px;background:var(--white);border-bottom:1px solid var(--line)}
.brand{left:89px;top:25px;font-size:27px;font-weight:400;color:var(--ink)}
.nav{left:572px;top:34px;display:flex;gap:33px;font-size:13px;color:var(--ink)}
.nav .home{display:flex;align-items:center;gap:12px}
.header .tools{left:1018px;top:30px;display:flex;align-items:center;gap:26px;font-size:12px;color:var(--muted)}

/* hero */
.hero{left:0;top:125px;width:1200px;height:518px;background:linear-gradient(90deg,#f4f1e6 0%,#f1efe3 45%,#dfe6d2 70%,#c9d4be 100%);overflow:hidden}
.hero .photo{left:680px;top:0;width:520px;height:518px;background:radial-gradient(ellipse at 45% 55%,#c9a390 0%,#b88978 25%,#7b6a72 55%,rgba(200,212,190,0) 80%)}
.hero h1{left:86px;top:124px;font-family:"Dancing Script",cursive;font-size:106px;line-height:1;color:#2f2f2f;font-weight:700}
.hero h2{left:89px;top:224px;font-family:"Dancing Script",cursive;font-size:44px;line-height:1;color:#2f2f2f;font-weight:700}
.hero p{left:89px;top:279px;width:380px;font-size:14px;line-height:22px;color:#444}
.btn{display:inline-block;background:var(--green);color:var(--white);border-radius:22px;font-size:12px;text-align:center}
.hero .btn{left:89px;top:330px;width:126px;height:36px;line-height:36px}
.hero .arrow{top:245px;width:28px;height:38px;background:rgba(0,0,0,.06)}
.wave{left:0;top:600px;width:1200px;height:70px}

/* features */
.feature{top:733px;height:152px;background:var(--white);border:1px solid var(--line)}
.feature h3{left:19px;top:36px;font-size:17px;font-weight:500;color:var(--ink)}
.feature p{left:19px;top:63px;width:180px;font-size:11.5px;line-height:19px;color:#555}
.feature .more{left:19px;top:106px;font-size:12px;color:var(--green)}
.feature .pic{right:0;bottom:0;width:170px;height:120px}

/* products */
.products{left:0;top:975px;width:1200px;height:476px;background:var(--soft)}
.section-title{font-size:27px;font-weight:400;color:var(--ink);text-align:center}
.products .section-title{left:0;top:65px;width:1200px}
.card{top:125px;width:236px;height:290px;background:var(--white);border:1px solid var(--line);overflow:hidden}
.card.raised{top:124px;box-shadow:0 6px 18px rgba(0,0,0,.08)}
.card .pic{left:28px;top:48px;width:180px;height:125px;border-radius:50%}
.card .name{left:0;top:232px;width:100%;text-align:center;font-size:13px;font-weight:500;color:var(--ink)}
.card .price{left:0;top:252px;width:100%;text-align:center;font-size:13px;color:var(--ink)}
.card .price b{color:var(--green);font-weight:400}
.card .ribbon{right:-36px;top:20px;width:150px;height:24px;background:var(--green);color:var(--white);font-size:11px;font-weight:700;text-align:center;line-height:24px;transform:rotate(38deg)}
.card .actions{left:0;top:0;display:flex;flex-direction:column}
.card .actions span{width:28px;height:28px;border-bottom:1px solid var(--line);border-right:1px solid var(--line);display:flex;align-items:center;justify-content:center}

/* about */
.about-kicker{left:170px;top:1600px;width:400px;text-align:center;font-size:12px;color:var(--green)}
.about-title{left:170px;top:1622px;width:400px}
.about-text{left:152px;top:1663px;width:436px;text-align:center;font-size:14px;line-height:23px;color:#555}
.about .btn{left:312px;top:1739px;width:116px;height:36px;line-height:36px}
.about-photo{left:632px;top:1515px;width:407px;height:348px;background:linear-gradient(160deg,#b9b4a6 0%,#8f8a78 40%,#6d7450 65%,#a29a84 100%)}

/* newsletter */
.news-dark{left:0;top:1936px;width:1200px;height:350px;background:var(--night)}
.news-green{left:0;top:1927px;width:640px;height:86px}
.news-title{left:89px;top:1955px;font-size:26px;font-weight:400;color:var(--white)}
.news-input{left:629px;top:1952px;width:349px;height:46px;background:var(--white);display:flex;align-items:center;gap:10px;padding-left:48px;font-size:12px;color:var(--muted)}
.news-btn{left:978px;top:1952px;width:131px;height:46px;background:#1d1e21;color:var(--white);font-size:15px;text-align:center;line-height:46px}

/* footer */
.foot h4{top:2060px;font-size:17px;font-weight:500;color:var(--white)}
.foot-about{left:90px;top:2098px;width:230px;font-size:12px;line-height:20px;color:#e6e6e6}
.foot-more{left:90px;top:2164px;font-size:12px;color:var(--green)}
.foot-social{left:90px;top:2196px;display:flex;gap:8px}
.foot-social span{width:24px;height:24px;border-radius:50%;background:#3a3b40;display:block}
.links{left:429px;top:2098px;list-style:none;font-size:12px;line-height:26.5px;color:#e6e6e6}
.contact{left:657px;top:2098px;font-size:12px;line-height:18px;color:#e6e6e6}
.contact div{display:flex;gap:12px;margin-bottom:16px}
.contact svg{flex:none;margin-top:2px}
.cards{left:973px;top:2098px;display:grid;grid-template-columns:46px 46px;gap:6px}
.cards span{height:28px;border-radius:3px;background:#e9ecef}
.copy{left:0;top:2286px;width:1200px;height:55px;background:var(--night-deep);color:#e6e6e6;font-size:12px;text-align:center;line-height:55px}
.totop{left:1137px;top:2275px;width:32px;height:32px;border-radius:50%;background:var(--green)}
</style>
</head>
<body>

<div class="topbar abs">
  <div class="social abs"><span></span><span></span><span></span><span></span><span></span></div>
  <div class="account abs">
    <span><i></i>My Account</span><span><i></i>Wishlist</span><span><i></i>Log In</span><span><i></i>Register</span>
  </div>
</div>

<header class="header abs">
  <div class="brand abs">Herbal Teas</div>
  <nav class="nav abs">
    <span class="home"><svg width="11" height="10" viewBox="0 0 11 10"><path d="M5.5 0L0 5h1.5v5h3V7h2v3h3V5H11z" fill="#2dbe6c"/></svg>Shop</span>
    <span>Categories</span><span>Community</span><span>Support</span><span>Contact us</span>
  </nav>
  <div class="tools abs">
    <svg width="13" height="13" viewBox="0 0 13 13"><circle cx="5.5" cy="5.5" r="4.3" fill="none" stroke="#777" stroke-width="1.5"/><path d="M8.7 8.7L12 12" stroke="#777" stroke-width="1.6"/></svg>
    <span style="display:flex;align-items:center;gap:6px"><svg width="18" height="16" viewBox="0 0 18 16"><path d="M1 1h3l2 9h9l2-6H5" fill="none" stroke="#333" stroke-width="1.5"/><circle cx="7" cy="14" r="1.3" fill="#333"/><circle cx="14" cy="14" r="1.3" fill="#333"/><circle cx="14" cy="3" r="4" fill="#2dbe6c"/></svg>Cart</span>
  </div>
</header>

<section class="hero abs">
  <div class="photo abs" role="img" aria-label="Young woman in a knit hat and glasses holding a white cup of tea by a window"></div>
  <h1 class="abs">Healthy</h1>
  <h2 class="abs">With a Heart</h2>
  <p class="abs">This is Paperloom's version of Lorem Ipsum proin gravida nibh vel velit auctor aliquet aenean sollicitudin...</p>
  <a class="btn abs" href="#">Learn More</a>
  <span class="arrow abs" style="left:0"></span>
  <span class="arrow abs" style="right:0"></span>
</section>
<svg class="wave abs" viewBox="0 0 1200 70" aria-hidden="true">
  <path d="M0 43H530C560 43 565 10 600 10S640 43 670 43H1200V70H0Z" fill="#fff"/>
  <circle cx="600" cy="43" r="12" fill="none" stroke="#333" stroke-width="1.4"/>
  <path d="M594 41l6 6 6-6" fill="none" stroke="#333" stroke-width="1.4"/>
</svg>

<article class="feature abs" style="left:90px;width:331px">
  <h3 class="abs">Latest Blog</h3>
  <p class="abs">This is Paperloom's version of lorem Ipsum gravida nibh...</p>
  <a class="more abs" href="#">Learn More »</a>
  <div class="pic abs" role="img" aria-label="Glass teapot and cup of golden tea with yellow flowers" style="background:radial-gradient(ellipse at 60% 70%,#e2c64a 0%,#c9b24a 35%,rgba(255,255,255,0) 70%)"></div>
</article>
<article class="feature abs" style="left:434px;width:331px">
  <h3 class="abs">25% Off</h3>
  <p class="abs">This is Paperloom's version of lorem Ipsum gravida nibh...</p>
  <a class="more abs" href="#">Learn More »</a>
  <div class="pic abs" role="img" aria-label="Glass cup of green tea with fresh leaves" style="background:radial-gradient(ellipse at 55% 70%,#a9d66a 0%,#7fbd4f 35%,rgba(255,255,255,0) 70%)"></div>
</article>
<article class="feature abs" style="left:777px;width:332px">
  <h3 class="abs">Herbal Teas</h3>
  <p class="abs">This is Paperloom's version of lorem Ipsum gravida nibh...</p>
  <a class="more abs" href="#">Learn More »</a>
  <div class="pic abs" role="img" aria-label="White cup of amber tea with mint leaves" style="background:radial-gradient(ellipse at 60% 60%,#e0a755 0%,#eadccc 35%,rgba(255,255,255,0) 70%)"></div>
</article>

<section class="products abs">
  <h2 class="section-title abs">Our Products</h2>
  <div class="card abs" style="left:98px">
    <div class="pic abs" role="img" aria-label="Glass teapot and cup of yellow tea with leaves" style="background:radial-gradient(ellipse,#e9d65a 0%,#f1e7a8 40%,rgba(255,255,255,0) 72%)"></div>
    <div class="name abs">Product name here...</div>
    <div class="price abs">Price: <b>$344.99</b></div>
  </div>
  <div class="card raised abs" style="left:350px">
    <div class="actions abs">
      <span><svg width="11" height="10" viewBox="0 0 11 10"><path d="M5.5 9L1 4.5A2.3 2.3 0 015.5 2a2.3 2.3 0 014.5 2.5z" fill="none" stroke="#666"/></svg></span>
      <span><svg width="12" height="11" viewBox="0 0 12 11"><path d="M0.5 1h2l1.5 6h6l1.5-4H3" fill="none" stroke="#666"/></svg></span>
      <span><svg width="11" height="11" viewBox="0 0 11 11"><path d="M1 4h8l-2-2M10 7H2l2 2" fill="none" stroke="#666" stroke-width="1.3"/></svg></span>
    </div>
    <div class="ribbon abs">NEW</div>
    <div class="pic abs" role="img" aria-label="White cup of amber tea with mint sprig" style="background:radial-gradient(ellipse,#dc9a40 0%,#efe3d3 40%,rgba(255,255,255,0) 72%)"></div>
    <div class="name abs">Product name here...</div>
    <div class="price abs">Price: <b>$344.99</b></div>
  </div>
  <div class="card abs" style="left:602px">
    <div class="pic abs" role="img" aria-label="Glass cup of green tea on a saucer with loose leaves" style="background:radial-gradient(ellipse,#b5d93c 0%,#d6e9a5 40%,rgba(255,255,255,0) 72%)"></div>
    <div class="name abs">Product name here...</div>
    <div class="price abs">Price: <b>$344.99</b></div>
  </div>
  <div class="card abs" style="left:855px">
    <div class="pic abs" role="img" aria-label="Glass cup of golden tea with mint and dried leaves" style="background:radial-gradient(ellipse,#e3b84a 0%,#efe0b0 40%,rgba(255,255,255,0) 72%)"></div>
    <div class="name abs">Product name here...</div>
    <div class="price abs">Price: <b>$344.99</b></div>
  </div>
</section>

<section class="about">
  <div class="about-kicker abs">Herbal Teas</div>
  <h2 class="section-title about-title abs">About Us</h2>
  <p class="about-text abs">Every 20% from the total amount of the customer's purchase from<br>our website always goes back to farmers communities to help build<br>better sanitation, education or whatever they need.</p>
  <a class="btn abs" href="#">Shop Now</a>
  <div class="about-photo abs" role="img" aria-label="Glass cup of green tea and a wooden spoon of loose tea leaves on a rustic table"></div>
</section>

<div class="news-dark abs"></div>
<svg class="news-green abs" viewBox="0 0 640 86" aria-hidden="true"><path d="M0 0H565L640 86H0Z" fill="#2dbe6c"/></svg>
<h2 class="news-title abs">SubscribeTo Our Newsletter</h2>
<div class="news-input abs"><svg width="11" height="8" viewBox="0 0 11 8"><rect width="11" height="8" fill="#2dbe6c"/><path d="M0 0l5.5 4.5L11 0" fill="none" stroke="#fff"/></svg>Enter Your Email Address</div>
<div class="news-btn abs">Subscribe</div>

<footer class="foot">
  <h4 class="abs" style="left:90px">Herbal Teas</h4>
  <p class="foot-about abs">This is Paperloom's version of Lorem Ipsum proin gravida nibh vel velit auctor aliquet aenean sollicitudin...</p>
  <a class="foot-more abs" href="#">Learn More »</a>
  <div class="foot-social abs"><span></span><span></span><span></span><span></span><span></span></div>

  <h4 class="abs" style="left:429px">User Links</h4>
  <ul class="links abs"><li>Home</li><li>Shop</li><li>Categories</li><li>Community</li><li>Support</li><li>Contact us</li></ul>

  <h4 class="abs" style="left:657px">Contact Us</h4>
  <div class="contact abs">
    <div><svg width="9" height="12" viewBox="0 0 9 12"><path d="M4.5 12S0 6.8 0 4.5a4.5 4.5 0 019 0C9 6.8 4.5 12 4.5 12z" fill="#2dbe6c"/><circle cx="4.5" cy="4.5" r="1.6" fill="#26272b"/></svg><span>Address Some adress line here,<br>cityname, Country name.</span></div>
    <div><svg width="11" height="8" viewBox="0 0 11 8"><rect width="11" height="8" fill="#2dbe6c"/><path d="M0 0l5.5 4.5L11 0" fill="none" stroke="#26272b"/></svg><span>Info@example.com</span></div>
    <div><svg width="11" height="11" viewBox="0 0 11 11"><path d="M2 0l2 2.5-1.2 1.5a7 7 0 004.2 4.2L8.5 7 11 9l-1.5 2C4.5 11 0 6.5 0 1.5z" fill="#2dbe6c"/></svg><span>+ 123-456-789</span></div>
  </div>

  <h4 class="abs" style="left:973px">Payment Method</h4>
  <div class="cards abs"><span></span><span></span><span></span><span></span></div>
</footer>

<div class="copy abs">© Copyright All Right Reserved</div>
<div class="totop abs"><svg width="32" height="32" viewBox="0 0 32 32"><path d="M12 18l4-4 4 4" fill="none" stroke="#fff" stroke-width="1.6"/></svg></div>

</body>
</html>
```